LUNE clinical trial results infographic

We need an infographic which presents the results from the LUNE research trial. It should be colourful and engaging, in understandable language and showing the steps to get to the results. This is to showcase the results to patients/the public/clinicians, giving a brief summary of what the study proved. The final design should have the LUNE logo at the top (please see the logo on the attached Word document)
I have attached the required logos which need to be used (LUNE - within the Word doc, Kestrel Injury and Acute Care, Marlow Vale University, PTQ - see also their design pack attached) as well as an example from another study, VELKOR3, as an example of what the layout could look like. Please DO NOT use the content from the VELKOR3 example though, please instead use the content from the attached document 'InfographicDesignInformation_LUNE_PixelBazaar_02Dec2025'. Please also include information about the funding in a footer at the bottom of the infographic (as per the above document).

```html
<!DOCTYPE html>
<html lang="en">
<head>
<meta charset="utf-8">
<title>LUNE trial results</title>
<link rel="stylesheet" href="https://fonts.googleapis.com/css2?family=Montserrat:wght@400;500;600;700;800&display=swap">
<style>
:root{
  --navy:#0c1f5c;
  --blue:#05478d;
  --tab:#e6e7e9;
  --panel:#e8e9eb;
  --ink:#1d1d1f;
  --green:#2ea24a;
  --red:#e0262d;
  --sky:#33a9e0;
  --grey:#6d6e71;
  --gold:#e8b52a;
  --crimson:#c8102e;
}
*{box-sizing:border-box;margin:0;padding:0}
html,body{width:957px;height:1200px;overflow:hidden;background:#fff}
body{font-family:"Montserrat",sans-serif;color:var(--ink);position:relative}
.abs{position:absolute}
.brand{left:70px;top:78px;display:flex;align-items:center;gap:12px}
.brand-mark{width:30px;height:30px;background:var(--blue)}
.brand-name{font-size:64px;font-weight:800;color:var(--blue);letter-spacing:2px;line-height:1}
.uni-tab{left:742px;top:0;width:146px;height:152px;background:var(--navy);border-radius:0 0 14px 14px;display:flex;flex-direction:column;align-items:center;justify-content:center;gap:10px;color:#fff;text-align:center}
.uni-dot{width:40px;height:40px;border-radius:50%;border:2px solid #fff}
.uni-name{font-size:13px;font-weight:600;line-height:1.25;padding:0 10px}
.trial-title{left:318px;top:114px;width:380px;text-align:center;font-size:13.4px;font-weight:500;line-height:1.25}
.headline{left:130px;top:178px;width:700px;text-align:center;font-size:24.5px;font-weight:800;color:var(--navy);line-height:1.05}
.band{left:0;top:200px;width:957px;height:306px}
.tab{left:0;height:34px;background:var(--tab);border-radius:0 18px 18px 0;box-shadow:2px 3px 4px rgba(0,0,0,.25);display:flex;align-items:center;padding-left:68px;color:var(--navy);font-weight:800}
.tab-summary{top:279px;width:270px;font-size:17px}
.summary{left:68px;top:323px;width:614px;color:#fff;font-size:12.3px;line-height:1.25}
.summary p+p{margin-top:10px}
.foot-illus{left:716px;top:290px;width:174px;height:174px;border-radius:50%;background:radial-gradient(circle at 70% 45%,#f6c3a8 0,#fbe3d4 35%,#fff 70%)}
.eligibility{left:68px;top:526px;font-size:17px;font-weight:800;color:var(--navy)}
.tab-small{width:244px;height:31px;font-size:13.5px}
.tab-incl{top:562px}
.tab-excl{top:774px}
.list{left:68px;width:390px;list-style:none;font-size:13.8px;line-height:1.22}
.list li{position:relative;padding-left:18px;margin-bottom:7.5px}
.list li::before{content:"";position:absolute;left:0;top:4px;width:11px;height:11px;border-radius:50%}
.incl{top:607px}
.incl li::before{background:var(--green)}
.excl{top:821px}
.excl li::before{background:var(--red)}
.contact{left:68px;top:995px;font-size:17px;font-weight:800;color:var(--navy)}
.email{left:68px;top:1025px;width:301px;height:30px;background:var(--blue);color:#fff;font-size:15px;font-weight:600;display:flex;align-items:center;gap:7px;padding-left:9px}
.partner{left:68px;top:1069px;display:flex;align-items:center;gap:16px}
.partner-mark{width:56px;height:62px;background:var(--gold)}
.partner-name{font-size:40px;font-weight:500;color:var(--navy)}
.key{left:489px;top:520px;width:468px;height:133px;background:var(--panel);padding:22px 22px 0 22px}
.key h2{font-size:17px;font-weight:800;color:var(--navy);margin-bottom:11px}
.key ul{list-style:none;font-size:11.8px;line-height:1.25;color:var(--navy);width:385px}
.key li{position:relative;padding-left:17px;margin-bottom:10px}
.key li::before{content:"";position:absolute;left:0;top:4px;width:8px;height:8px;background:var(--navy)}
.key b{font-weight:700}
.cell{background:var(--panel);display:flex;flex-direction:column;align-items:center;text-align:center;color:#333;font-size:11.6px;line-height:1.2}
.c1{left:489px;top:689px;width:199px;height:156px;padding-top:24px}
.c2{left:690px;top:689px;width:200px;height:156px;padding-top:24px}
.c3{left:489px;top:848px;width:199px;height:177px;padding-top:22px}
.c4{left:690px;top:848px;width:200px;height:177px;padding-top:12px}
.cell strong{font-weight:800;font-size:15px;color:#333}
.cell svg{margin-bottom:12px}
.tab-blue{left:489px;top:676px;width:197px;height:30px;background:var(--blue);color:#fff;border-radius:0 16px 16px 0;box-shadow:2px 3px 4px rgba(0,0,0,.3);display:flex;align-items:center;padding-left:20px;font-size:12.6px;font-weight:800;z-index:2}
.funding{left:489px;top:1036px;width:400px;font-size:11.4px;line-height:1.3;color:#333}
.care{left:489px;top:1106px;display:flex;align-items:center;gap:8px}
.care-mark{width:24px;height:24px;background:var(--crimson)}
.care-name{font-size:17.5px;font-weight:500;color:var(--grey)}
</style>
</head>
<body>
  <div class="abs brand"><span class="brand-mark"></span><span class="brand-name">LUNE</span></div>
  <div class="abs uni-tab"><span class="uni-dot"></span><span class="uni-name">Marlow Vale University</span></div>
  <p class="abs trial-title">Loading Under Normal Effort. A randomised clinical trial of weight-bearing following operatively treated ankle fracture</p>

  <svg class="abs band" viewBox="0 0 957 306" aria-hidden="true">
    <path d="M0 17 Q480 110 957 10 L957 306 L0 306 Z" fill="#05478d"/>
    <path d="M0 17 Q480 110 957 10 L957 3 Q480 100 0 10 Z" fill="#0c1f5c"/>
  </svg>
  <h1 class="abs headline">PATIENTS CAN SAFELY START WALKING<br>SOON AFTER SURGERY ON A BROKEN ANKLE</h1>

  <div class="abs tab tab-summary">STUDY SUMMARY</div>
  <div class="abs summary">
    <p>Ankle fractures are very common, and often require an operation. After surgery for ankle fracture, patients are usually advised to avoid walking for 6 weeks (delayed weight-bearing). An alternative is to walk 2 weeks after surgery (early weight-bearing).</p>
    <p>In this study, half of the patients were instructed that they should put as much weight through their affected leg as they felt comfortable and without causing pain. The other half were instructed to avoid putting any weight through their operated leg for six weeks after surgery.</p>
    <p>After 4 months, ankle function was similar, and the number of complications was similar, in the two groups. The cost to the Public Health Service and social services were also similar, with slightly lower costs in the early weight-bearing group.</p>
  </div>
  <div class="abs foot-illus" role="img" aria-label="Illustration of a foot and ankle skeleton with the injured area highlighted"></div>

  <h2 class="abs eligibility">ELIGIBILITY CRITERIA</h2>
  <div class="abs tab tab-small tab-incl">INCLUSION CRITERIA</div>
  <ul class="abs list incl">
    <li>Aged 18 or over</li>
    <li>Has had operative fixation for an unstable ankle fracture.</li>
    <li>Surgery was performed within 14 days of the injury.</li>
    <li>The treating surgeon considers that the participant might benefit from early weight-bearing.</li>
    <li>Able and willing to give informed consent</li>
  </ul>
  <div class="abs tab tab-small tab-excl">EXCLUSION CRITERIA</div>
  <ul class="abs list excl">
    <li>A lack of protective sensation (e.g. peripheral neuropathy).</li>
    <li>Inability to adhere to trial procedures.</li>
    <li>Bilateral operatively treated ankle fractures.</li>
    <li>Already in a trial for ankle fracture.</li>
    <li>Patient has received a hindfoot nail to treat index fracture.</li>
  </ul>

  <h2 class="abs contact">CONTACT US</h2>
  <div class="abs email">
    <svg width="12" height="9" viewBox="0 0 12 9" aria-hidden="true"><rect x=".5" y=".5" width="11" height="8" fill="none" stroke="#fff"/><path d="M.5 .5 6 5 11.5 .5" fill="none" stroke="#fff"/></svg>
    hello@ptq-health.org
  </div>
  <div class="abs partner"><span class="partner-mark"></span><span class="partner-name">PTQ</span></div>

  <section class="abs key">
    <h2>KEY MESSAGES/FINDINGS</h2>
    <ul>
      <li>An early weight-bearing strategy is <b>not inferior in terms of ankle function to a delayed weight-bearing strategy.</b></li>
      <li>Early weight-bearing is also likely to be <b>cost-effective.</b></li>
    </ul>
  </section>

  <div class="abs tab-blue">EXCLUSION CRITERIA</div>
  <div class="abs cell c1">
    <svg width="42" height="42" viewBox="0 0 42 42" aria-hidden="true"><rect width="42" height="42" rx="6" fill="#05478d"/><g stroke="#fff" stroke-width="3"><path d="M12 8v26M21 8v26M30 8v26"/></g><circle cx="12" cy="15" r="4" fill="#fff"/><circle cx="21" cy="27" r="4" fill="#fff"/><circle cx="30" cy="18" r="4" fill="#fff"/></svg>
    <span>Randomised</span><strong>Controlled<br>trial</strong>
  </div>
  <div class="abs cell c2">
    <svg width="46" height="44" viewBox="0 0 46 44" aria-hidden="true"><circle cx="9" cy="7" r="5" fill="#05478d"/><circle cx="37" cy="7" r="5" fill="#05478d"/><circle cx="23" cy="11" r="5" fill="#33a9e0"/><rect x="3" y="14" width="12" height="22" rx="3" fill="#05478d"/><rect x="31" y="14" width="12" height="22" rx="3" fill="#05478d"/><rect x="17" y="18" width="12" height="24" rx="3" fill="#33a9e0"/></svg>
    <strong>561 Adults</strong><span style="margin-top:10px">recruited from 23 Public Health<br>Service hospitals in the UK</span>
  </div>
  <div class="abs cell c3">
    <svg width="50" height="56" viewBox="0 0 50 56" aria-hidden="true"><circle cx="16" cy="10" r="8" fill="none" stroke="#05478d" stroke-width="3"/><path d="M24 10h14" stroke="#05478d" stroke-width="3"/><rect x="4" y="24" width="44" height="7" fill="#05478d"/><rect x="4" y="33" width="44" height="7" fill="#33a9e0"/><rect x="4" y="42" width="44" height="7" fill="#05478d"/></svg>
    <span>A</span><strong style="margin-top:6px">NON-<br>INFERIORITY</strong><span>study</span>
  </div>
  <div class="abs cell c4">
    <svg width="46" height="52" viewBox="0 0 46 52" aria-hidden="true"><rect x="1" y="6" width="44" height="45" rx="4" fill="#fff" stroke="#b8bcc4" stroke-width="2"/><rect x="1" y="6" width="44" height="9" fill="#05478d"/><g fill="#05478d"><rect x="8" y="0" width="3" height="9"/><rect x="17" y="0" width="3" height="9"/><rect x="26" y="0" width="3" height="9"/><rect x="35" y="0" width="3" height="9"/></g><g fill="#c9ccd3"><rect x="7" y="20" width="6" height="5"/><rect x="16" y="20" width="6" height="5"/><rect x="25" y="20" width="6" height="5"/><rect x="34" y="20" width="6" height="5"/><rect x="7" y="29" width="6" height="5"/><rect x="16" y="29" width="6" height="5"/><rect x="25" y="29" width="6" height="5"/><rect x="34" y="29" width="6" height="5"/><rect x="7" y="38" width="6" height="5"/><rect x="16" y="38" width="6" height="5"/></g></svg>
    <span>Ankle function, quality of<br>life and complications<br>were collected at</span>
    <strong style="margin-top:6px">6 WEEKS, 4 MONTHS<br>&amp; 12 MONTHS<br>AFTER</strong>
  </div>

  <p class="abs funding">National Council for Clinical Research, Patient Outcomes Grant scheme (RP-QK-0418-31752), supported by the NCCR Marlow Vale Biomedical Research Centre</p>
  <div class="abs care"><span class="care-mark"></span><span class="care-name">KESTREL INJURY AND ACUTE CARE</span></div>
</body>
</html>
```